Price list for young Relaxon clinic

I require a price list/Treatment menu for clinic

To include:
Logo
Address
Phone number
Website

List of services and Prices
Relaxon 1 area £100
Relaxon 2 areas £150
Relaxon 3 areas £200
Lip Enhancement 0.5ml £100
Lip Enhancement 1ml £200
Facial Fillers £200 per 1ml
Volumiq £450 per session (2 vials - must be bought as a course)
Non Surgical Face Lift (Thread Lift) £600 per area
Skin Press Full Face £250
Skin Press Small Per Small Area £100
Cryo Therapy £60
Chemical Peel Light Peel and Microdermabrasion £85
Chemical Peel Deep Peel £150
Consultation £30 redeemable against service
Relaxon Top Up Relaxon £50 (must be within 2 weeks of 1st treatment)
Filler Top Up £100 (must be within 2 weeks of 1st appointment)

Open Hours
Updates

Company Name: HVM Address: 482 Pellbrook Road, 6 Warnford High Street, KT4 3JQ Phone: 0208 947 2186 Website: www.hollyvanmereaesthetics.co.uk

Please add more colour

Needs to be much cleaner and simpler Front page to include logo and price list Back page to inculde open hours and contact information including google map. Please no images with needles. Images of lips and faces are good, but try not to crowd copy on the pagei. No copy on top of images. White, grey, black and reds are good on colouring.

Target Market(s)

young market ages 22-45 years old mainly female
modern

Industry/Entity Type

Clinic

Number of Pages Required

4 page

Requirements
Must have
• Logo - logo must be in colour grey/silver
• Address (small map?)
• Phone number
• Web address
• Services
• Open hours
• Prices
• Images

```html
<!DOCTYPE html>
<html lang="en">
<head>
<meta charset="utf-8">
<title>Price List - Holly Vanmere Aesthetics</title>
<link rel="stylesheet" href="https://fonts.googleapis.com/css2?family=Alegreya+Sans:wght@400;500&family=Overlock:wght@400&display=swap">
<style>
  :root {
    --page-bg: #e0dfdf;
    --band-light: #a5a6a9;
    --band-dark: #8c8b8d;
    --price-red: #c2373d;
    --footer-red: #9d3238;
    --footer-grey: #8f8f91;
    --brand-grey: #a3a3a3;
    --white: #ffffff;
    --photo-left: linear-gradient(160deg, #d9d3cf 0%, #cbb8ac 45%, #c9c5c2 100%);
    --photo-right: linear-gradient(200deg, #e4ddd3 0%, #d9c2aa 40%, #d7d1c9 100%);
  }
  * { margin: 0; padding: 0; box-sizing: border-box; }
  html, body { width: 846px; height: 1200px; overflow: hidden; background: var(--page-bg); }
  .sheet { position: relative; width: 846px; height: 1200px; background: var(--page-bg); font-family: "Alegreya Sans", sans-serif; }

  .photo { position: absolute; top: 0; height: 275px; }
  .photo--left { left: 0; width: 271px; background: var(--photo-left); }
  .photo--right { left: 584px; width: 262px; background: var(--photo-right); }

  .brand { position: absolute; left: 271px; width: 313px; top: 22px; text-align: center; color: var(--brand-grey); font-family: "Overlock", sans-serif; font-weight: 400; }
  .brand__mark { display: flex; align-items: center; justify-content: center; gap: 12px; height: 110px; }
  .brand__dot { width: 16px; height: 16px; border-radius: 50%; background: var(--brand-grey); }
  .brand__initials { font-size: 46px; letter-spacing: 4px; }
  .brand__name { margin-top: 14px; font-size: 24px; letter-spacing: 3px; line-height: 1; }
  .brand__sub { font-size: 36px; letter-spacing: 3px; line-height: 1.05; }

  .list-title { position: absolute; top: 278px; left: 0; width: 846px; text-align: center; color: var(--price-red); font-family: "Overlock", sans-serif; font-size: 27px; letter-spacing: 2px; }

  .price-list { position: absolute; top: 314px; left: 0; width: 846px; list-style: none; }
  .price-row { display: flex; align-items: center; height: 32px; margin-bottom: 6.4px; color: var(--white); background: var(--band-light); }
  .price-row--dark { background: var(--band-dark); }
  .price-row__name { padding-left: 77px; width: 622px; font-size: 21px; }
  .price-row__price { color: var(--price-red); font-size: 26px; white-space: pre; }
  .price-note { height: 38.4px; display: flex; align-items: flex-start; padding-left: 77px; padding-top: 2px; color: var(--white); font-size: 21px; }

  .footer { position: absolute; left: 0; top: 1040px; width: 846px; height: 160px; }
  .footer__shape { position: absolute; inset: 0; }
  .footer__contact { position: absolute; left: 120px; top: 36px; color: var(--white); }
  .footer__address, .footer__phone { font-size: 22px; line-height: 36px; }
  .footer__web { font-size: 19px; letter-spacing: 3.2px; line-height: 26px; }
  .footer__map { position: absolute; left: 550px; top: 78px; width: 165px; height: 66px; background: linear-gradient(135deg, #e8e6e1, #d9d6cf); border: 1px solid #c9c7c2; }
</style>
</head>
<body>
<div class="sheet">
  <div class="photo photo--left" role="img" aria-label="Portrait of a woman with facial contour lift arrows"></div>
  <div class="brand">
    <div class="brand__mark"><span class="brand__dot"></span><span class="brand__initials">HVM</span></div>
    <div class="brand__name">HOLLY VANMERE</div>
    <div class="brand__sub">AESTHETICS</div>
  </div>
  <div class="photo photo--right" role="img" aria-label="Portrait of a blonde woman with hands at her face"></div>

  <h1 class="list-title">Price List - Holly Vanmere Aesthetics</h1>

  <ul class="price-list">
    <li class="price-row"><span class="price-row__name">Relaxon 1 area</span><span class="price-row__price">£100</span></li>
    <li class="price-row price-row--dark"><span class="price-row__name">Relaxon 2 areas</span><span class="price-row__price">£150</span></li>
    <li class="price-row"><span class="price-row__name">Relaxon 3 areas</span><span class="price-row__price">£200</span></li>
    <li class="price-row price-row--dark"><span class="price-row__name">Lip Enhancement 0.5ml</span><span class="price-row__price">£100</span></li>
    <li class="price-row"><span class="price-row__name">Lip Enhancement 1ml</span><span class="price-row__price">£200</span></li>
    <li class="price-row price-row--dark"><span class="price-row__name">Facial Fillers 1ml</span><span class="price-row__price">£200</span></li>
    <li class="price-row"><span class="price-row__name">Volumiq per session</span><span class="price-row__price">£450</span></li>
    <li class="price-note">(2 vials - must be bought as a course)</li>
    <li class="price-row"><span class="price-row__name">Non Surgical Face Lift (Thread Lift)per area</span><span class="price-row__price">£600</span></li>
    <li class="price-row price-row--dark"><span class="price-row__name">Skin Press Full Face</span><span class="price-row__price">£250</span></li>
    <li class="price-row"><span class="price-row__name">Skin Press Small Per Small Area</span><span class="price-row__price">£100</span></li>
    <li class="price-row price-row--dark"><span class="price-row__name">Cryo Therapy</span><span class="price-row__price">£  60</span></li>
    <li class="price-row"><span class="price-row__name">Chemical Peel Light Peel and Microdermabrasion</span><span class="price-row__price">£  85</span></li>
    <li class="price-row price-row--dark"><span class="price-row__name">Chemical Peel Deep Peel</span><span class="price-row__price">£150</span></li>
    <li class="price-row"><span class="price-row__name">Consultation redeemable against service</span><span class="price-row__price">£  30</span></li>
    <li class="price-row price-row--dark"><span class="price-row__name">Relaxon Top Up Relaxon</span><span class="price-row__price">£  50</span></li>
    <li class="price-note">(must be within 2 weeks of 1st treatment)</li>
    <li class="price-row"><span class="price-row__name">Filler Top Up</span><span class="price-row__price">£100</span></li>
    <li class="price-note">(must be within 2 weeks of 1st appointment)</li>
  </ul>

  <footer class="footer">
    <svg class="footer__shape" width="846" height="160" viewBox="0 0 846 160" aria-hidden="true">
      <path d="M0 40 Q423 -22 846 40 L846 160 L0 160 Z" fill="var(--footer-grey)"/>
      <path d="M0 47 Q423 -12 846 47 L846 160 L0 160 Z" fill="var(--footer-red)"/>
    </svg>
    <div class="footer__contact">
      <p class="footer__address">HVM Address: 482 Pellbrook Road, 6 Warnford High Street, KT4 3JQ</p>
      <p class="footer__phone">Phone: 0208 947 2186</p>
      <p class="footer__web">www.hollyvanmereaesthetics.co.uk</p>
    </div>
    <div class="footer__map" role="img" aria-label="Small street map showing the clinic location on Warnford Parade"></div>
  </footer>
</div>
</body>
</html>
```